Tailbrook - eCommerce Design and Shopify Theme customisation

eCommerce Website Design - firstly with mockups then once we have chosen the design the successful designer will need to choose, purchase and customise a Shopify theme to match the design. We have a logo already designed and now want to create our web presence based on carrying up to 50 products on our website.
Target Market(s)
UK Pet Owners
Industry/Entity Type
Pet Shop
Requirements
Must have
- Design must be achievable using a customised Shopify theme - the successful designer will be responsible for the delivery of a working theme on our shopify website.
Should not have
- should not look cheap or have designs that aren't compatible or achievable with Shopify

```html
<!DOCTYPE html>
<html lang="en">
<head>
<meta charset="utf-8">
<title>Tailbrook – Pet Shop</title>
<link href="https://fonts.googleapis.com/css2?family=Poppins:wght@400;500;600;700&family=Oswald:wght@400;500&display=swap" rel="stylesheet">
<style>
:root{
  --teal:#45b49d;
  --teal-dark:#3aa08b;
  --gold:#d6b23d;
  --gold-dark:#c29e2c;
  --cream:#fbf7e8;
  --ink:#222;
  --grey:#777;
  --light:#eee;
  --red:#e0362c;
  --footer:#2d2d2d;
  --white:#fff;
}
*{box-sizing:border-box;margin:0;padding:0}
html,body{width:1200px;height:5143px;overflow:hidden}
body{font-family:"Poppins",sans-serif;color:var(--ink);background:var(--white);position:relative}
.abs{position:absolute}
.ph{position:absolute}

/* header */
.topbar{left:0;top:0;width:1200px;height:113px;background:var(--white)}
.lang{left:105px;top:10px;font-size:11px;color:var(--grey)}
.socials-top{left:200px;top:8px;display:flex;gap:6px}
.socials-top span{width:14px;height:14px;border-radius:50%;background:#bbb;display:block}
.contact-link{left:110px;top:74px;font-size:14px}
.brand{left:520px;top:18px;width:160px;text-align:center}
.brand-dot{width:46px;height:46px;border-radius:50%;background:var(--gold);margin:0 auto 6px}
.brand-name{font-size:26px;font-weight:600;color:var(--gold-dark);line-height:1}
.pet-btn{top:58px;height:36px;border:2px solid var(--light);font-size:13px;font-weight:500;display:flex;align-items:center;gap:8px;padding:0 14px}
.pet-btn i{width:18px;height:18px;border-radius:50%;background:var(--gold);display:block}
.account{left:946px;top:10px;font-size:11px;color:var(--grey);display:flex;gap:20px}
.search{left:945px;top:68px;width:160px;height:26px;border-bottom:1px solid var(--light);font-size:11px;color:#aaa}
.search svg{position:absolute;right:4px;top:4px}
.nav{left:0;top:113px;width:1200px;height:42px;background:var(--gold);display:flex;align-items:center;justify-content:space-between;padding:0 115px}
.nav a{color:var(--ink);text-decoration:none;font-size:14px;font-weight:500}

/* hero */
.hero{left:0;top:155px;width:1200px;height:500px;background:var(--teal);overflow:hidden}
.hero-title{left:340px;top:90px;font-size:58px;font-weight:600;color:var(--white);line-height:1.15}

/* shop for */
.choose{left:0;top:655px;width:1200px;height:528px;background:var(--cream)}
.choose-card{top:65px;width:309px;height:394px;background:var(--gold);box-shadow:0 4px 10px rgba(0,0,0,.15)}
.choose-card .frame{position:absolute;inset:14px;border:2px solid var(--white)}
.choose-card h3{position:absolute;left:0;right:0;top:40px;text-align:center;color:var(--white);font-size:36px;font-weight:700;line-height:1.2}
.choose-card .ph{left:80px;top:150px;width:150px;height:200px;border-radius:6px}

/* section headings */
.sec-title{left:0;width:1200px;text-align:center;font-size:40px;font-weight:700;letter-spacing:.5px}
.sec-sub{left:0;width:1200px;text-align:center;font-size:12px;color:var(--grey)}

/* products */
.product{width:224px;height:360px;background:var(--white);border:1px solid var(--light)}
.product .ph{left:12px;top:12px;width:198px;height:220px}
.add-cart{position:absolute;left:12px;top:232px;width:198px;height:26px;background:var(--gold);color:var(--white);font-size:11px;display:flex;align-items:center;justify-content:center}
.price{position:absolute;left:0;right:0;top:280px;text-align:center;font-size:18px}
.price s{color:var(--red);margin-right:8px}
.p-name{position:absolute;left:0;right:0;top:306px;text-align:center;font-size:14px}
.dots{position:absolute;left:0;right:0;top:332px;display:flex;justify-content:center;gap:5px}
.dots span{width:8px;height:8px;border-radius:50%;background:#555}
.dots span.off{background:#ccc}
.arrow{font-size:40px;color:var(--gold);line-height:1}

/* promo */
.promo{left:0;top:2383px;width:1200px;height:446px;background:var(--teal)}
.promo-pack{left:120px;top:20px;width:300px;height:420px;border-radius:8px}
.promo-title{left:465px;top:90px;font-size:64px;font-weight:600;color:var(--white)}
.promo-title em{font-style:normal;color:var(--gold)}
.promo-range{left:465px;top:178px;font-size:48px;font-weight:600;color:var(--gold)}
.promo-text{left:465px;top:252px;width:560px;font-size:19px;font-weight:500;color:var(--white);line-height:1.45}
.buy-btn{left:465px;top:370px;width:170px;height:50px;border-radius:25px;background:var(--gold);color:var(--white);font-size:15px;font-weight:600;display:flex;align-items:center;justify-content:center}
.promo-phone{left:665px;top:372px;font-size:32px;font-weight:600;color:var(--white)}

/* testimonials */
.quote-card{top:3137px;width:320px;height:360px;background:var(--white);box-shadow:0 4px 14px rgba(0,0,0,.12);text-align:center}
.quote-mark{position:absolute;left:0;top:0;width:40px;height:40px;background:var(--gold);color:var(--white);font-size:34px;font-weight:700;line-height:50px}
.avatar{position:absolute;left:125px;top:30px;width:70px;height:70px;border-radius:50%}
.quote-card p{position:absolute;left:28px;right:28px;top:128px;font-size:12px;color:#555;line-height:1.65}
.q-name{position:absolute;left:0;right:0;top:280px;font-size:14px;color:var(--gold-dark)}
.q-role{position:absolute;left:0;right:0;top:302px;font-size:11px;color:var(--grey)}

/* blog */
.blog{left:0;top:3583px;width:1200px;height:686px;background:var(--gold)}
.blog .sec-sub{color:#5a4a14}
.post-main{left:113px;top:140px;width:470px;height:480px;background:var(--white)}
.post-main .ph{left:0;top:0;width:470px;height:290px}
.meta{font-size:10px;color:var(--grey)}
.post-h{font-weight:600;line-height:1.3}
.more{font-size:10px;color:var(--gold-dark);font-weight:600}
.post-side{left:617px;width:470px;height:180px}
.post-side .ph{left:0;top:0;width:150px;height:180px}
.post-side .box{position:absolute;left:150px;top:0;width:320px;height:180px;background:var(--white);padding:22px}

/* newsletter */
.stay{left:190px;top:4389px;width:920px;height:223px;background:var(--cream);border:3px solid var(--gold)}
.stay-dog{left:1040px;top:4330px;width:90px;height:90px;border-radius:8px}
.stay-left{left:50px;top:30px;width:290px;text-align:center}
.stay-left .kick{font-size:13px;color:#555}
.stay-left h3{font-family:"Oswald",sans-serif;font-weight:400;font-size:40px;letter-spacing:1px}
.stay-left p{font-size:11px;color:#666;line-height:1.5}
.divider{left:410px;top:30px;width:1px;height:160px;background:var(--gold)}
.paw{left:395px;top:95px}
.email{left:460px;top:60px;width:330px;height:38px;background:var(--white);border:1px solid #ddd;font-size:11px;color:#aaa;padding:11px 16px}
.go{left:790px;top:60px;width:50px;height:38px;background:var(--gold);color:var(--white);font-size:13px;font-weight:600;display:flex;align-items:center;justify-content:center}
.follow{left:560px;top:116px;font-size:14px}
.social-row{left:520px;top:148px;display:flex;gap:14px}
.social-row span{width:36px;height:36px;border-radius:50%;background:#333;display:block}

/* footer */
.footer{left:0;top:4697px;width:1200px;height:446px;background:var(--footer);color:#ccc}
.f-col{top:40px}
.f-col h4{font-size:15px;font-weight:500;color:var(--white);margin-bottom:14px;letter-spacing:.5px}
.f-col li{list-style:none;font-size:11px;line-height:22px}
.f-col li::before{content:"› ";color:var(--gold)}
.c-row{display:flex;gap:10px;align-items:flex-start;font-size:11px;margin-bottom:12px;line-height:1.5}
.c-row b{color:var(--white);font-weight:500}
.f-brand{left:940px;top:105px;text-align:center}
.f-brand .brand-dot{width:40px;height:40px}
.f-brand .brand-name{color:var(--gold);font-size:22px}
.pay-strip{left:110px;top:190px;width:980px;height:188px;background:var(--white);padding:22px 28px;color:var(--ink)}
.pay-strip h5{font-size:14px;font-weight:600;margin-bottom:16px}
.badges{display:flex;gap:10px}
.badges span{display:block;height:32px;border-radius:4px}
.copy{left:0;top:408px;width:1200px;text-align:center;font-size:10px;color:#999}
</style>
</head>
<body>

<header class="abs topbar">
  <div class="abs lang">English ▾</div>
  <div class="abs socials-top"><span></span><span></span><span></span><span></span></div>
  <div class="abs contact-link">Contact</div>
  <div class="abs pet-btn" style="left:365px"><i></i>FOR DOG</div>
  <div class="abs brand"><div class="brand-dot"></div><div class="brand-name">Tailbrook</div></div>
  <div class="abs pet-btn" style="left:695px"><i></i>FOR CAT</div>
  <div class="abs account"><span>Cart (0)</span><span>Login</span></div>
  <div class="abs search">Search
    <svg width="14" height="14" viewBox="0 0 14 14"><circle cx="6" cy="6" r="4.5" fill="none" stroke="#555" stroke-width="1.6"/><line x1="9.5" y1="9.5" x2="13" y2="13" stroke="#555" stroke-width="1.6"/></svg>
  </div>
</header>
<nav class="abs nav"><a>HOME</a><a>DOG</a><a>CAT</a><a>SHOP</a><a>BLOGS</a><a>CONTACTS</a></nav>

<section class="abs hero">
  <div class="ph" role="img" aria-label="Black automatic pet food feeder with a bowl of kibble" style="left:100px;top:40px;width:210px;height:380px;background:linear-gradient(#3a3a3a,#1c1c1c);border-radius:14px"></div>
  <h1 class="abs hero-title">Automatic<br>Dog Feeder</h1>
  <div class="ph" role="img" aria-label="Dalmatian dog lying beside a grey tabby kitten" style="left:690px;top:0;width:510px;height:470px;background:radial-gradient(circle at 60% 55%,#f4f4f4,#cfd6d4 70%,var(--teal) 100%)"></div>
</section>

<section class="abs choose">
  <div class="abs choose-card" style="left:274px"><div class="frame"></div><h3>SHOP FOR<br>YOUR DOG</h3>
    <div class="ph" role="img" aria-label="White line illustration of a sitting dog" style="background:rgba(255,255,255,.25)"></div></div>
  <div class="abs choose-card" style="left:610px"><div class="frame"></div><h3>SHOP FOR<br>YOUR CAT</h3>
    <div class="ph" role="img" aria-label="White line illustration of a sitting cat" style="background:rgba(255,255,255,.25)"></div></div>
</section>

<h2 class="abs sec-title" style="top:1260px">FEATURED PRODUCTS</h2>
<p class="abs sec-sub" style="top:1314px">Fresh favourites picked by our team for happy, healthy pets this season.</p>
<div class="abs arrow" style="left:70px;top:1505px">‹</div>
<div class="abs arrow" style="left:1100px;top:1505px">›</div>
<div class="abs product" style="left:120px;top:1389px"><div class="ph" role="img" aria-label="Bag of dry dog food" style="background:linear-gradient(#5d8fb0,#7a4b2e)"></div><div class="price"><s>$25.00</s>$20.00</div><div class="p-name">Lorem ipsum dolor</div><div class="dots"><span></span><span></span><span></span><span class="off"></span></div></div>
<div class="abs product" style="left:370px;top:1389px"><div class="ph" role="img" aria-label="Bag of cat food with a tabby cat" style="background:linear-gradient(#dfe6ec,#6f9bb8)"></div><div class="add-cart">ADD TO CART</div><div class="price"><s>$25.00</s>$20.00</div><div class="p-name">Lorem ipsum dolor</div><div class="dots"><span></span><span></span><span></span><span class="off"></span></div></div>
<div class="abs product" style="left:620px;top:1389px"><div class="ph" role="img" aria-label="Box of dental dog treats" style="background:linear-gradient(#3e8a3a,#2c6a2a)"></div><div class="price"><s>$25.00</s>$20.00</div><div class="p-name">Lorem ipsum dolor</div><div class="dots"><span></span><span></span><span></span><span class="off"></span></div></div>
<div class="abs product" style="left:870px;top:1389px"><div class="ph" role="img" aria-label="Steel pet water fountain with a cat drinking" style="background:linear-gradient(#d9d9d9,#8a8a8a)"></div><div class="price"><s>$25.00</s>$20.00</div><div class="p-name">Lorem ipsum dolor</div><div class="dots"><span></span><span></span><span></span><span class="off"></span></div></div>

<h2 class="abs sec-title" style="top:1820px">NEW ARRIVALS</h2>
<p class="abs sec-sub" style="top:1874px">Just landed in store: new treats, toys and feeding kit for dogs and cats.</p>
<div class="abs arrow" style="left:70px;top:2065px">‹</div>
<div class="abs arrow" style="left:1100px;top:2065px">›</div>
<div class="abs product" style="left:120px;top:1954px"><div class="ph" role="img" aria-label="Bag of dry dog food" style="background:linear-gradient(#5d8fb0,#7a4b2e)"></div><div class="price"><s>$25.00</s>$20.00</div><div class="p-name">Lorem ipsum dolor</div><div class="dots"><span></span><span></span><span></span><span class="off"></span></div></div>
<div class="abs product" style="left:370px;top:1954px"><div class="ph" role="img" aria-label="Bag of cat food with a tabby cat" style="background:linear-gradient(#dfe6ec,#6f9bb8)"></div><div class="add-cart">ADD TO CART</div><div class="price"><s>$25.00</s>$20.00</div><div class="p-name">Lorem ipsum dolor</div><div class="dots"><span></span><span></span><span></span><span class="off"></span></div></div>
<div class="abs product" style="left:620px;top:1954px"><div class="ph" role="img" aria-label="Puppy lying down chewing a green toy" style="background:linear-gradient(#f6efe4,#c98f4f)"></div><div class="price"><s>$25.00</s>$20.00</div><div class="p-name">Lorem ipsum dolor</div><div class="dots"><span></span><span></span><span></span><span class="off"></span></div></div>
<div class="abs product" style="left:870px;top:1954px"><div class="ph" role="img" aria-label="Steel pet water fountain with a cat drinking" style="background:linear-gradient(#d9d9d9,#8a8a8a)"></div><div class="price"><s>$25.00</s>$20.00</div><div class="p-name">Lorem ipsum dolor</div><div class="dots"><span></span><span></span><span></span><span class="off"></span></div></div>

<section class="abs promo">
  <div class="ph promo-pack" role="img" aria-label="Yellow bag of dry cat food with a cat on the front" style="background:linear-gradient(135deg,#f3c531,#c7861e)"></div>
  <div class="abs promo-title">Save up to <em>40%</em></div>
  <div class="abs promo-range">$120 - $200</div>
  <p class="abs promo-text">Lorem ipsum dolor sit amet, consectetuer adipiscin elit, sed diam nonummy nibh euismod tincidunt ut laoreet dolore magna aliquam.</p>
  <div class="abs buy-btn">BUY NOW</div>
  <div class="abs promo-phone">+44 1632 960 450</div>
</section>

<h2 class="abs sec-title" style="top:3005px">CLIENT TESTIMONIALS</h2>
<p class="abs sec-sub" style="top:3059px">Kind words from pet owners across the UK who shop with us every month.</p>
<div class="abs quote-card" style="left:120px"><div class="quote-mark">“</div><div class="avatar" role="img" aria-label="Customer portrait" style="background:#c9b6a6"></div><p>Lorem ipsum dolor sit a non adipiscing elit, sed diam nonum nibbles tincidunt laoreet magna aliam erat volut paer anim sed qui mini veniam, quis nostrud labore ullamcorper.</p><div class="q-name">Customer Name</div><div class="q-role">Dolor Nonum Nibbeno Tincidunt</div></div>
<div class="abs quote-card" style="left:440px"><div class="quote-mark">“</div><div class="avatar" role="img" aria-label="Customer portrait" style="background:#c9b6a6"></div><p>Lorem ipsum dolor sit a non adipiscing elit, sed diam nonum nibbles tincidunt laoreet magna aliam erat volut paer anim sed qui mini veniam, quis nostrud labore ullamcorper.</p><div class="q-name">Customer Name</div><div class="q-role">Dolor Nonum Nibbeno Tincidunt</div></div>
<div class="abs quote-card" style="left:760px"><div class="quote-mark">“</div><div class="avatar" role="img" aria-label="Customer portrait" style="background:#c9b6a6"></div><p>Lorem ipsum dolor sit a non adipiscing elit, sed diam nonum nibbles tincidunt laoreet magna aliam erat volut paer anim sed qui mini veniam, quis nostrud labore ullamcorper.</p><div class="q-name">Customer Name</div><div class="q-role">Dolor Nonum Nibbeno Tincidunt</div></div>

<section class="abs blog">
  <h2 class="abs sec-title" style="top:58px">NEWS BLOG</h2>
  <p class="abs sec-sub" style="top:110px">Care tips, feeding guides and shop news from the Tailbrook team.</p>
  <article class="abs post-main">
    <div class="ph" role="img" aria-label="Woman relaxing at home cuddling her cat" style="background:linear-gradient(135deg,#e9e1d6,#b49a82)"></div>
    <div class="abs meta" style="left:24px;top:305px">By Admin &nbsp;|&nbsp; 12 June 2024</div>
    <div class="abs post-h" style="left:24px;top:330px;width:420px;font-size:22px">Lorem Ipsum Dolor Sit , Consectetuer Adipiscing Elit.</div>
    <div class="abs more" style="left:24px;top:400px">CONTINUE READING »</div>
  </article>
  <article class="abs post-side" style="top:205px">
    <div class="ph" role="img" aria-label="Woman hugging her dog on a sofa" style="background:linear-gradient(135deg,#e7d8c3,#a88767)"></div>
    <div class="box"><div class="meta">By Admin &nbsp;|&nbsp; 12 June 2024</div><div class="post-h" style="font-size:20px;margin:10px 0">Lorem Ipsum Dolor Sit Adipiscing Elit.</div><div class="more">CONTINUE READING »</div></div>
  </article>
  <article class="abs post-side" style="top:411px">
    <div class="ph" role="img" aria-label="Owner with a small terrier dog" style="background:linear-gradient(135deg,#efe6d9,#b69a7a)"></div>
    <div class="box"><div class="meta">By Admin &nbsp;|&nbsp; 12 June 2024</div><div class="post-h" style="font-size:20px;margin:10px 0">Lorem Ipsum Dolor Sit Adipiscing Elit.</div><div class="more">CONTINUE READING »</div></div>
  </article>
</section>

<section class="abs stay">
  <div class="abs stay-left"><div class="kick">Like, Follow, Sign up...</div><h3>STAY IN TOUCH</h3><p>Get news on offers and new arrivals, plus simple pet care tips sent to your inbox.</p></div>
  <div class="abs divider"></div>
  <svg class="abs paw" width="28" height="28" viewBox="0 0 28 28" style="background:var(--cream)"><ellipse cx="14" cy="19" rx="6" ry="5" fill="#333"/><circle cx="7" cy="11" r="2.6" fill="#333"/><circle cx="11.5" cy="6.5" r="2.6" fill="#333"/><circle cx="16.5" cy="6.5" r="2.6" fill="#333"/><circle cx="21" cy="11" r="2.6" fill="#333"/></svg>
  <div class="abs email">ENTER YOUR EMAIL ADDRESS</div>
  <div class="abs go">GO</div>
  <div class="abs follow">Follow Us</div>
  <div class="abs social-row"><span></span><span></span><span></span><span></span></div>
</section>
<div class="ph stay-dog" role="img" aria-label="Small terrier dog peeking over the box" style="background:linear-gradient(#f1ebe2,#b89e80)"></div>

<footer class="abs footer">
  <div class="abs f-col" style="left:113px"><h4>QUICK LINKS</h4><ul><li>Home</li><li>Dog</li><li>Cat</li><li>Blog</li><li>Contact</li></ul></div>
  <div class="abs f-col" style="left:413px"><h4>MY ACCOUNT</h4><ul><li>About</li><li>Orders</li><li>Wishlist</li><li>Returns</li><li>FAQ</li></ul></div>
  <div class="abs f-col" style="left:703px"><h4>CONTACT INFO</h4>
    <div class="c-row"><svg width="12" height="14" viewBox="0 0 12 14"><path d="M6 0C2.7 0 0 2.6 0 5.8 0 10 6 14 6 14s6-4 6-8.2C12 2.6 9.3 0 6 0z" fill="var(--gold)"/><circle cx="6" cy="5.8" r="2" fill="var(--footer)"/></svg><div><b>Main Office</b><br>12 Brook Lane, Leeds</div></div>
    <div class="c-row"><svg width="12" height="12" viewBox="0 0 12 12"><path d="M2 0h2l1 3-1.5 1a7 7 0 0 0 4.5 4.5L9 7l3 1v2c0 1-1 2-2 2A10 10 0 0 1 0 2C0 1 1 0 2 0z" fill="var(--gold)"/></svg>01632 960 451</div>
    <div class="c-row"><svg width="14" height="10" viewBox="0 0 14 10"><rect width="14" height="10" rx="1" fill="var(--gold)"/><path d="M0 1l7 5 7-5" fill="none" stroke="var(--footer)" stroke-width="1.2"/></svg>hello@tailbrook.co.uk</div>
  </div>
  <div class="abs f-brand"><div class="brand-dot"></div><div class="brand-name">Tailbrook</div></div>
  <div class="abs pay-strip">
    <div class="abs" style="left:28px;top:22px"><h5>Methods of Payment</h5>
      <div class="badges"><span style="width:50px;background:#1a3e8c"></span><span style="width:44px;background:#e84a2c"></span><span style="width:44px;background:#2d7fc1"></span><span style="width:60px;background:#1b4a8a"></span><span style="width:66px;background:#333"></span></div></div>
    <div class="abs" style="left:470px;top:22px"><h5>Delivery Partners</h5>
      <div class="badges"><span style="width:54px;background:#d02424"></span><span style="width:54px;background:#c8102e"></span><span style="width:54px;background:#b22"></span><span style="width:54px;background:#e02b2b"></span><span style="width:40px;background:#d33"></span><span style="font-size:10px;height:auto;line-height:1.4"><b>Free Delivery</b><br>for UK orders over £30</span></div></div>
  </div>
  <div class="abs copy">© All Rights Reserved. Tailbrook 2024</div>
</footer>

</body>
</html>
```